Keen Volt Electrical in need of a business card design

We need a new business card designed for our electrical business. We have a logo already which I will attach below.
Would like the business card to be..
-BLACK background preferably, possibly white back ground behind logo if colours clash.
-White & Blue (logo blue) text
Something that makes the logo pop, & a modern look. Possibly minimal clean format.

REQUIRE:
-Logo on front & back

TEXT TO INCLUDE (ON ONE SIDE):

Tom Harlow
Director/Electrician
M: 0412 563 718
E:info@keenvoltelectrical.com.au
W:www.keenvoltelectrical.com.au
R.E.C 58431

Custom/New Homes
Renovations
Commercial Office/Shop Fit-outs
Communications & Security Cameras
Electric Vehicle Chargers
Airconditioning
Updates

Requirements
Nice to have
• Possibly even lighten the grey shades for the words 'Keen' & 'Volt' to be more easily read on a black background.

```html
<!DOCTYPE html>
<html lang="en">
<head>
<meta charset="utf-8">
<title>Keen Volt Electrical – Business Card</title>
<link rel="stylesheet" href="https://fonts.googleapis.com/css2?family=Exo+2:ital,wght@0,500;0,600;0,700;1,400&family=Mulish:wght@400;500&display=swap">
<style>
  :root {
    --backdrop: #e4e4e4;
    --card: #060606;
    --band: #131313;
    --band-soft: #0d0d0d;
    --blue: #1ba3e0;
    --white: #ffffff;
    --grey: #8a8f96;
    --logo-grey: #c9ced4;
  }
  * { margin: 0; padding: 0; box-sizing: border-box; }
  html, body {
    width: 1200px; height: 960px; overflow: hidden;
    background: var(--backdrop);
  }
  .card {
    position: absolute; left: 277px; width: 645px; height: 410px;
    background: var(--card); overflow: hidden;
    box-shadow: 0 4px 10px rgba(0,0,0,.25);
    font-family: "Exo 2", sans-serif;
  }
  .card--front { top: 44px; }
  .card--back { top: 484px; }
  .bands { position: absolute; inset: 0; width: 100%; height: 100%; }

  .brand {
    position: absolute; left: 72px; top: 70px;
    display: flex; align-items: center; gap: 16px;
  }
  .brand__mark { width: 34px; height: 34px; background: var(--blue); }
  .brand__name {
    font-size: 36px; font-weight: 700; color: var(--logo-grey);
    letter-spacing: -0.3px; white-space: nowrap;
  }

  .holder { position: absolute; left: 34px; top: 200px; }
  .holder__name { font-size: 26px; font-weight: 600; color: var(--blue); line-height: 1.1; }
  .holder__role { font-size: 16px; font-style: italic; font-weight: 400; color: var(--grey); margin-top: 2px; }

  .contact {
    position: absolute; display: flex; align-items: center; gap: 9px;
    font-family: "Mulish", sans-serif; font-size: 15.5px; color: var(--white);
    white-space: nowrap;
  }
  .contact svg { width: 16px; height: 16px; flex: none; }
  .contact--phone { left: 28px; top: 337px; }
  .contact--email { left: 28px; top: 367px; }
  .contact--web { left: 344px; top: 334px; }
  .contact--licence { left: 344px; top: 364px; }

  .service {
    position: absolute; width: 260px; margin-left: -130px;
    text-align: center; color: var(--white);
    font-size: 22px; font-weight: 600; line-height: 28px;
  }
  .service svg { display: block; margin: 0 auto 6px; width: 36px; height: 36px; }
  .col-a { left: 192px; }
  .col-b { left: 465px; }
  .row-1 { top: 36px; }
  .row-2 { top: 140px; }
  .row-3 { top: 274px; }
</style>
</head>
<body>

<section class="card card--front" aria-label="Card front">
  <svg class="bands" viewBox="0 0 645 410" aria-hidden="true">
    <polygon points="120,0 230,0 645,415 645,410 535,410" fill="var(--band-soft)"/>
    <polygon points="300,0 400,0 610,210 560,260" fill="var(--band)"/>
    <polygon points="440,0 530,0 645,115 645,205" fill="var(--band)"/>
    <polygon points="0,60 0,160 250,410 350,410" fill="var(--band-soft)"/>
  </svg>

  <div class="brand">
    <span class="brand__mark"></span>
    <span class="brand__name">Keen Volt Electrical</span>
  </div>

  <div class="holder">
    <p class="holder__name">Tom Harlow</p>
    <p class="holder__role">Director/Electrician</p>
  </div>

  <p class="contact contact--phone">
    <svg viewBox="0 0 16 16" fill="none" stroke="var(--blue)" stroke-width="1.4"><path d="M4 1.5l2.2 3-1.4 1.6c.8 1.9 2.3 3.4 4.2 4.3l1.6-1.4 3 2.2-1.3 2.6C7 13.5 2.4 9 1.5 3z"/></svg>
    0412 563 718
  </p>
  <p class="contact contact--email">
    <svg viewBox="0 0 16 16" fill="none" stroke="var(--blue)" stroke-width="1.3"><circle cx="8" cy="8" r="6.5"/><ellipse cx="8" cy="8" rx="2.8" ry="6.5"/><path d="M1.5 8h13M2.5 4.8h11M2.5 11.2h11"/></svg>
    info@keenvoltelectrical.com.au
  </p>
  <p class="contact contact--web">
    <svg viewBox="0 0 16 16" fill="none" stroke="var(--blue)" stroke-width="1.4"><rect x="1.5" y="3.5" width="13" height="9"/><path d="M1.5 3.5L8 9l6.5-5.5"/></svg>
    www.keenvoltelectrical.com.au
  </p>
  <p class="contact contact--licence">
    <svg viewBox="0 0 16 16" fill="none" stroke="var(--blue)" stroke-width="1.4"><path d="M8 15s5-5 5-8.5a5 5 0 0 0-10 0C3 10 8 15 8 15z"/><circle cx="8" cy="6.5" r="1.8"/></svg>
    R.E.C 58431
  </p>
</section>

<section class="card card--back" aria-label="Card back">
  <svg class="bands" viewBox="0 0 645 410" aria-hidden="true">
    <polygon points="40,0 150,0 560,410 450,410" fill="var(--band-soft)"/>
    <polygon points="330,0 430,0 645,215 595,265" fill="var(--band)"/>
    <polygon points="0,120 0,230 180,410 290,410" fill="var(--band-soft)"/>
    <polygon points="470,0 560,0 645,85 645,175" fill="var(--band)"/>
  </svg>

  <div class="service col-a row-1">
    <svg viewBox="0 0 36 36" fill="none" stroke="var(--blue)" stroke-width="1.8" stroke-linejoin="round"><path d="M4 17L18 4l14 13M8 14v17h20V14M15 31v-8h6v8"/></svg>
    Custom/New Homes
  </div>
  <div class="service col-b row-1">
    <svg viewBox="0 0 36 36" fill="none" stroke="var(--blue)" stroke-width="1.8" stroke-linejoin="round"><path d="M8 30l13-13a6 6 0 0 0 7-8l-4 4-3-1-1-3 4-4a6 6 0 0 0-8 7L3 25z"/></svg>
    Renovations
  </div>
  <div class="service col-a row-2">
    <svg viewBox="0 0 36 36" fill="none" stroke="var(--blue)" stroke-width="1.8" stroke-linejoin="round"><path d="M11 34V12l8-3V3l6 9v22zM15 20h4M15 24h4M15 28h4"/></svg>
    Commercial<br>Office/Shop Fit-outs
  </div>
  <div class="service col-b row-2">
    <svg viewBox="0 0 36 36" fill="none" stroke="var(--blue)" stroke-width="1.8" stroke-linejoin="round"><rect x="7" y="8" width="24" height="11" rx="2"/><path d="M3 10v7h4M24 19v6h-4M20 25a2 2 0 1 0 0 .1"/></svg>
    Communications &amp;<br>Security Cameras
  </div>
  <div class="service col-a row-3">
    <svg viewBox="0 0 36 36" fill="none" stroke="var(--blue)" stroke-width="1.8" stroke-linejoin="round"><path d="M6 24v-6l4-6h14l5 6 4 1v5h-2M8 24h18"/><circle cx="11" cy="25" r="3"/><circle cx="28" cy="25" r="3"/><path d="M4 20V12l3-3"/></svg>
    Electric Vehicle<br>Chargers
  </div>
  <div class="service col-b row-3">
    <svg viewBox="0 0 36 36" fill="none" stroke="var(--blue)" stroke-width="1.8" stroke-linecap="round"><path d="M24 8v20M15 18h18M18 12l12 12M30 12L18 24M21 8l3 3 3-3M21 28l3-3 3 3M8 10v12M2 16h12M4 12l8 8M12 12l-8 8"/></svg>
    Airconditioning
  </div>
</section>

</body>
</html>
```